HOLLOWAY SOUND: Community What happens when crime comes to an island town?

I have a vision of the cover on my 6" x 9", shelfwise ready, book cover front as a picture of the town and mountains in black and white, perhaps the mountains in color, below it the ocean (blood red?), then the same town flipped like in a mirror to white to black to suggest the underlying crime in the town. On the back, to highlight the discovery and climax (#1 of 2 in this story) I included attachment of The Stone Hut in the forest. It's creepy as creepy gets! Author info and book blub, and bar code here. So, top half of front cover is normal beautiful shot (black and white) of a coastal town, a strip of blood-red ocean, then bottom half mirrored in black to reflect the crime underbelly of the town. The Stone Hut is the back cover for readers to figure out once they've read the novel.

The following is what I consider when I use Shelfwise tools to build a book cover (I realize this is basic) All of this is only if it works, not meant to corral your creativity—not my intention. I will trust your taste but I’m leaning toward the “soft underbelly of a normal coastal town” theme.

Book Theme:
the emotional core of this story is the desperate fight for the soul of a community.
the corrosive nature of long-buried secrets.
the blurred line between justice and revenge.

FRONT-B&W Top image ocean, town, mountains
Bottom-same image revers B&W (if it works)
Divider: strip of oceans between top and bottom in red and hopefully with some movement of the tide implied
tone, title: HOLLOWAY SOUND:
sub-title: COMMUNITY
“A novel by Martin Presby”
Somewhere on the cover the line: What happens when crime comes to a small-town?” I may change this
Spine same color scheme as cover: Title & subtitle, Author name publisher “Indie” at the moment
Back: split in half top/bottom
TOP: greys and the image of the wellhouse
Edges blended (and textured as rough paper if possible) around back of book and onto spine
Split line of red, as per the front
Author blurb below is: (can be shortened)
Martin Presby is a Canadian novelist whose crime fiction is steeped in the tides, timber, and tight-knit loyalties of the B.C. coast. Presby writes about ordinary people forced to choose between community and survival when power turns ruthless. Before studying English at Lindell Ridge University, he worked as a coast logger; later he built a career as a computer technologist and taught both privately and at the college level. Those experiences—boardrooms and boomtowns, classrooms and logging roads—give his stories their textured sense of place and the moral ambiguity that defines small-town noir. He has published seven novels and won first place (2013) and third place (2012) in the Northern Writers Guild’s PenQuest! national short story contest, with publications in The Marlow Quarterly, The Heron, and several Canadian anthologies. This is his first of a four-book crime series set in a coastal town where long-buried secrets surface with the tide.
Your credits
Publisher
Website for book
Bar code

Target Market(s)

This story is for adult readers who enjoy dark, gritty crime thrillers with a strong sense of place. Fans of character-driven narratives with morally complex protagonists, like those written by Gordon Varsley or Mira Holt, would connect deeply with the intricate web of corruption and secrets in a small town pushed to its breaking point. It will especially appeal to those who appreciate stories where the setting itself becomes a character.

Industry/Entity Type

crime thriller-mystery novels (fiction)

Font styles to use
Other font styles liked:
• I plan the interior to be Garamond

Requirements
Must have
• A sense of duality on the over, or more precisely, crime underlying the natural beauty of the town
Nice to have
• It would be nice if the ocean strip appeared as a river with movement implied

```html
<!DOCTYPE html>
<html lang="en">
<head>
<meta charset="utf-8">
<title>Holloway Sound – Full Cover Wrap</title>
<link rel="stylesheet" href="https://fonts.googleapis.com/css2?family=Bebas+Neue&family=Poppins:wght@400&family=PT+Serif:ital@1&display=swap">
<style>
  :root {
    --paper: #ffffff;
    --ink-dark: #1d1a18;
    --forest-top: #262220;
    --forest-mid: #302b27;
    --town-warm: #5a5048;
    --town-deep: #1f1c1a;
    --text-light: #ffffff;
    --rule: #cfcac4;
    --photo-slot: #4a4a4a;
  }
  * { margin: 0; padding: 0; box-sizing: border-box; }
  html, body { width: 1200px; height: 844px; overflow: hidden; background: var(--paper); }
  .wrap {
    position: absolute; left: 22px; top: 22px; width: 1156px; height: 800px;
    background: var(--ink-dark); overflow: hidden;
  }
  .scene-forest {
    position: absolute; left: 0; top: 0; width: 100%; height: 627px;
    background: linear-gradient(180deg, var(--forest-top) 0%, var(--forest-mid) 55%, #2a2623 80%, #1c1917 100%);
  }
  .scene-town {
    position: absolute; left: 0; top: 627px; width: 100%; height: 173px;
    background: linear-gradient(180deg, #3a332d 0%, var(--town-warm) 30%, #3c352f 60%, var(--town-deep) 100%);
  }
  .panel { position: absolute; top: 0; height: 100%; }
  .back { left: 0; width: 534px; }
  .spine { left: 534px; width: 89px; border-left: 1px solid #111; border-right: 1px solid #111; }
  .front { left: 623px; width: 533px; }

  /* back cover */
  .back-title {
    position: absolute; left: 0; width: 100%; top: 44px; text-align: center;
    font-family: "Bebas Neue", sans-serif; font-size: 48px; line-height: 0.9;
    color: var(--text-light); transform: skewY(-5deg);
  }
  .back-title span { display: block; background: linear-gradient(90deg, #8d8d8d, #fff 60%); -webkit-background-clip: text; background-clip: text; color: transparent; }
  .blurb {
    position: absolute; left: 58px; top: 158px; width: 398px;
    font-family: "Poppins", sans-serif; font-size: 10.6px; line-height: 14.8px;
    color: var(--text-light); text-align: justify;
  }
  .rule { position: absolute; left: 58px; width: 398px; height: 1px; background: var(--rule); }
  .rule.top { top: 438px; }
  .rule.bottom { top: 621px; }
  .author-photo { position: absolute; left: 62px; top: 459px; width: 113px; height: 142px; background: var(--photo-slot); }
  .author-bio {
    position: absolute; left: 191px; top: 462px; width: 265px;
    font-family: "Poppins", sans-serif; font-size: 10.6px; line-height: 14.8px;
    color: var(--text-light); text-align: justify;
  }
  .code-slot { position: absolute; left: 277px; top: 654px; width: 179px; height: 113px; background: var(--paper); }

  /* spine */
  .spine-text {
    position: absolute; left: 50%; top: 46px; transform: translateX(-50%);
    writing-mode: vertical-rl; white-space: nowrap;
    font-family: "Bebas Neue", sans-serif; font-size: 38px; letter-spacing: 1px;
    color: var(--text-light); line-height: 1;
  }
  .spine-text .novel { font-family: "PT Serif", serif; font-style: italic; font-size: 13px; margin: 22px 0 12px; letter-spacing: 0; }

  /* front cover */
  .tagline {
    position: absolute; left: 0; width: 100%; top: 78px; text-align: center;
    font-family: "Bebas Neue", sans-serif; font-size: 30px; line-height: 35px;
    letter-spacing: 1.5px; color: var(--text-light);
  }
  .front-title {
    position: absolute; left: 0; width: 100%; top: 270px; text-align: center;
    font-family: "Bebas Neue", sans-serif; font-size: 150px; line-height: 0.92;
    transform: skewY(-6deg);
  }
  .front-title span { display: block; background: linear-gradient(90deg, #9a9a9a 0%, #fff 45%, #fff 100%); -webkit-background-clip: text; background-clip: text; color: transparent; }
  .byline {
    position: absolute; left: 0; width: 100%; top: 690px; text-align: center;
    font-family: "PT Serif", serif; font-style: italic; font-size: 24px; color: var(--text-light);
  }
  .author-name {
    position: absolute; left: 0; width: 100%; top: 714px; text-align: center;
    font-family: "Bebas Neue", sans-serif; font-size: 64px; letter-spacing: 2px; color: var(--text-light);
  }
</style>
</head>
<body>
<div class="wrap">
  <div class="scene-forest" role="img" aria-label="Dark winter forest of bare tree trunks across the full wrap"></div>
  <div class="scene-town" role="img" aria-label="Mirrored reflection of a coastal town with houses and trees"></div>

  <section class="panel back">
    <h2 class="back-title"><span>HOLLOWAY</span><span>SOUND</span></h2>
    <div class="blurb">
      <p>Lorem ipsum dolor sit amet, consectetuer adipiscing elit, sed diam nonummy nibh euismod tincidunt ut laoreet dolore magna aliquam erat volutpat. Ut wisi enim ad minim veniam, quis nostrud exerci tation ullamcorper suscipit lobortis nisl ut aliquip ex ea commodo consequat. Duis autem vel eum iriure dolor in hendrerit in vulputate velit esse molestie consequat, vel illum dolore eu feugiat nulla facilisis at vero eros et accumsan et iusto odio dignissim qui blandit praesent luptatum zzril delenit augue duis dolore te feugait nulla facilisi.</p>
      <p>Lorem ipsum dolor sit amet, cons ectetuer adipiscing elit, sed diam nonummy nibh euismod tincidunt ut laoreet dolore magna aliquam erat volutpat. Ut wisi enim ad minim veniam, quis nostrud exerci tation ullamcorper suscipit lobortis nisl ut aliquip ex ea commodo consequat.</p>
      <p>Lorem ipsum dolor sit amet, consectetuer adipiscing elit, sed diam nonummy nibh euismod tincidunt ut laoreet dolore magna aliquam erat volutpat. Ut wisi enim ad minim veniam, quis nostrud exerci tation ullamcorper suscipit lobortis nisl ut aliquip ex ea</p>
    </div>
    <div class="rule top"></div>
    <div class="author-photo" role="img" aria-label="Author photo"></div>
    <p class="author-bio">Lorem ipsum dolor sit amet, consectetuer adipiscing elit, sed diam nonummy nibh euismod tincidunt ut laoreet dolore magna aliquam erat volutpat. Ut wisi enim ad minim veniam, quis nostrud exerci tation ullamcorper suscipit lobortis nisl ut aliquip ex ea commodo consequat. Duis autem vel eum iriure dolor in hendrerit in vulputate velit esse molestie consequat, vel illum dolore eu feugiat nulla facilisis at vero eros</p>
    <div class="rule bottom"></div>
    <div class="code-slot"></div>
  </section>

  <section class="panel spine">
    <div class="spine-text">HOLLOWAY SOUND COMMUNITY<span class="novel">A novel by</span>MARTIN PRESBY</div>
  </section>

  <section class="panel front">
    <p class="tagline">COMMUNITY WHAT HAPPENS WHEN<br>CRIME COMES TO AN ISLAND TOWN?</p>
    <h1 class="front-title"><span>HOLLOWAY</span><span>SOUND</span></h1>
    <p class="byline">A noval by</p>
    <p class="author-name">MARTIN PRESBY</p>
  </section>
</div>
</body>
</html>
```